Flint Yard Strategy Powerpoint Template

We require a powerpoint template, including an appropriate colour palette, for our marketing consultancy called "Flint Yard Strategy". We specialise in B2B Marketing & Innovation strategy for the life sciences and digital healthcare industries.
Our logo has already been designed and we have adopted two font styles for our communications so far: Bebas Neue and Bitter.
Our brand is heavily based around a contemporary industrial style and incorporates elements from east Londons design scene. In fact, our logo and brand was inspired by the street signs around flint yard in east London. Currently we use a template that uses various grey, black and off-white tones to reflect a industrial style and would like to keep clean creative innovative style. However, we are open to seeing additional colour proposals, as long as they retain the modern industrial feel.

Industry/Entity Type

Business Consultant

Colors

Designer to choose colors to be used in the design.

Requirements
Must have
• Our logo has already been designed and we have adopted two font styles for our communications so far: Bebas Neue and Bitter.
• Our brand is heavily based around a contemporary industrial style and incorporates elements from east Londons design scene. In fact, our logo and brand was inspired by the street signs around flint yard in east London.
• creative shapes and images to drop in
Nice to have
• owever, we are open to seeing additional colour proposals, as long as they retain the modern industrial feel
Should not have
• too corporate,

```html
<!DOCTYPE html>
<html lang="en">
<head>
<meta charset="utf-8">
<title>Flint Yard Strategy – Presentation Template</title>
<link rel="stylesheet" href="https://fonts.googleapis.com/css2?family=Bebas+Neue&family=Bitter:wght@400;600&family=Open+Sans:wght@400;600&display=swap">
<style>
:root{
  --ink:#1c1c1c;
  --char:#3a3a3a;
  --grey:#8c8c8c;
  --mist:#e6e6e6;
  --fog:#f4f4f4;
  --stone:#cdc3b2;
  --gold:#d6a53a;
  --paper:#ffffff;
  --canvas:#ffffff;
}
*{box-sizing:border-box;margin:0;padding:0}
html,body{width:1200px;height:2948px;overflow:hidden;background:var(--canvas)}
body{font-family:"Open Sans",Arial,sans-serif;color:var(--ink)}
.deck{display:grid;grid-template-columns:repeat(3,388px);grid-auto-rows:218px;gap:8.5px 8px;padding:6px 10px}
.slide{position:relative;overflow:hidden;background:var(--paper);box-shadow:0 0 0 1px #dcdcdc;padding:16px 20px}
.slide.dark{background:var(--ink);color:#fff}
.slide.gold{background:var(--gold)}
.slide.grey{background:#5a5a5a;color:#fff}
.tag{position:absolute;left:0;bottom:10px;width:28px;height:11px;background:var(--ink)}
.tag::after{content:"";position:absolute;left:6px;top:5px;width:14px;height:1px;background:#fff}
.dark .tag,.grey .tag{background:#fff}
.dark .tag::after,.grey .tag::after{background:var(--ink)}
.hd{font-family:"Bebas Neue",Impact,sans-serif;font-size:17px;letter-spacing:.5px;line-height:1}
.hd.lg{font-size:24px}
.sub{font-family:"Bitter",Georgia,serif;font-size:6px;color:var(--grey);margin-top:3px;line-height:1.4}
.p{font-family:"Bitter",Georgia,serif;font-size:5.5px;line-height:1.5;color:#666}
.dark .p,.grey .p{color:#bdbdbd}
.lbl{font-family:"Bebas Neue",Impact,sans-serif;font-size:10px;letter-spacing:.4px;line-height:1.1}
.logo{display:inline-flex;align-items:center;justify-content:center;background:var(--ink);color:#fff;font-family:"Bebas Neue",Impact,sans-serif;letter-spacing:2px;font-size:12px;padding:9px 12px;line-height:1}
.logo.inv{background:#fff;color:var(--ink)}
.photo{position:absolute;background:linear-gradient(160deg,#d8d8d8 0%,#8e8e8e 55%,#3d3d3d 100%)}
.photo.warm{background:linear-gradient(160deg,#7a6a55 0%,#3a342c 60%,#1a1714 100%)}
.photo.night{background:linear-gradient(180deg,#2d2d2d 0%,#5e5e5e 60%,#1c1c1c 100%)}
.abs{position:absolute}
.row{display:flex;gap:10px}
.col{flex:1}
.sq{width:16px;height:16px;background:var(--ink);flex:none}
.sq.g{background:var(--gold)}
.dot{width:12px;height:12px;border-radius:50%;background:var(--gold);flex:none}
.item{display:flex;gap:7px;align-items:flex-start;margin-bottom:8px}
.bar{height:14px;display:flex;align-items:center;padding:0 6px;color:#fff;font-family:"Bebas Neue",Impact,sans-serif;font-size:9px;margin-bottom:5px}
.card{background:var(--mist);padding:8px}
table{border-collapse:collapse;width:100%;font-size:5.5px;font-family:"Bitter",Georgia,serif}
th{background:var(--ink);color:#fff;font-weight:600;padding:3px;text-align:left}
td{padding:3px;border-bottom:1px solid var(--mist);color:#666}
tr:nth-child(even) td{background:var(--fog)}
</style>
</head>
<body>
<main class="deck">

<!-- 1 cover dark -->
<section class="slide dark">
  <div class="photo night" style="inset:0;opacity:.5" role="img" aria-label="Dark street scene backdrop"></div>
  <div class="abs" style="left:150px;top:86px"><span class="logo" style="border:1px solid #fff">FLINT YARD STRATEGY</span></div>
</section>

<!-- 2 cover light -->
<section class="slide" style="box-shadow:inset 0 0 0 1px var(--ink)">
  <span class="logo" style="margin-top:40px">FLINT YARD STRATEGY</span>
  <p class="hd" style="margin-top:14px">Your title of presentation goes here</p>
  <p class="sub">A short line to introduce this deck</p>
</section>

<!-- 3 cover photo -->
<section class="slide">
  <div class="photo" style="inset:0" role="img" aria-label="Grey city street photograph"></div>
  <div class="abs" style="right:40px;top:40px"><span class="logo">FLINT YARD STRATEGY</span></div>
  <span class="tag"></span>
</section>

<!-- 4 gold section -->
<section class="slide gold">
  <span class="logo" style="margin-top:50px">FLINT YARD STRATEGY</span>
  <p class="hd" style="margin-top:10px">Your title goes here</p>
  <p class="p" style="color:var(--ink)">Supporting line for this section</p>
  <span class="tag"></span>
</section>

<!-- 5 quote dark -->
<section class="slide dark" style="text-align:center">
  <svg width="22" height="22" viewBox="0 0 22 22" style="margin-top:28px"><circle cx="11" cy="11" r="11" fill="var(--gold)"/><path d="M7 13v-3l2-3h1l-1 3h1v3zm5 0v-3l2-3h1l-1 3h1v3z" fill="#1c1c1c"/></svg>
  <p class="hd" style="font-size:14px;margin:14px auto 0;max-width:250px">Great strategy is simple to say and hard to copy across every market we enter</p>
  <p class="p" style="margin-top:10px">Jane Doe</p>
  <span class="tag"></span>
</section>

<!-- 6 agenda -->
<section class="slide">
  <p class="hd">Our agenda</p>
  <p class="sub">A quick view of today's session</p>
  <div class="row" style="margin-top:14px">
    <div class="col">
      <div class="item"><span class="sq"></span><div><p class="lbl">Market insight</p><p class="p">Short note on this topic</p></div></div>
      <div class="item"><span class="sq"></span><div><p class="lbl">Brand position</p><p class="p">Short note on this topic</p></div></div>
      <div class="item"><span class="sq"></span><div><p class="lbl">Growth plan</p><p class="p">Short note on this topic</p></div></div>
    </div>
    <div class="col">
      <div class="item"><span class="sq"></span><div><p class="lbl">Audience</p><p class="p">Short note on this topic</p></div></div>
      <div class="item"><span class="sq"></span><div><p class="lbl">Channels</p><p class="p">Short note on this topic</p></div></div>
      <div class="item"><span class="sq"></span><div><p class="lbl">Next steps</p><p class="p">Short note on this topic</p></div></div>
    </div>
  </div>
  <span class="tag"></span>
</section>

<!-- 7 photo with text panel -->
<section class="slide">
  <div class="photo" style="inset:0" role="img" aria-label="Black and white photograph of a cathedral skyline"></div>
  <div class="abs" style="left:30px;top:40px;width:120px;height:110px;background:rgba(28,28,28,.85);padding:12px;color:#fff">
    <p class="hd" style="font-size:14px">Service area</p>
    <p class="p" style="color:#ccc;margin-top:6px">Short copy describing the service we offer here</p>
  </div>
  <span class="tag"></span>
</section>

<!-- 8 services -->
<section class="slide">
  <p class="hd">Our services</p>
  <div class="photo" style="left:20px;top:50px;width:150px;height:120px" role="img" aria-label="Grey office photograph"></div>
  <div class="abs" style="left:186px;top:52px;width:182px">
    <div class="item"><span class="sq"></span><div><p class="lbl">Strategy</p><p class="p">Short supporting copy for this point</p></div></div>
    <div class="item"><span class="sq"></span><div><p class="lbl">Innovation</p><p class="p">Short supporting copy for this point</p></div></div>
    <div class="item"><span class="sq"></span><div><p class="lbl">Insight</p><p class="p">Short supporting copy for this point</p></div></div>
  </div>
  <span class="tag"></span>
</section>

<!-- 9 quote area -->
<section class="slide">
  <p class="hd">Quote area</p>
  <p class="p" style="margin-top:40px;width:150px">A short statement that sets out our view on this subject</p>
  <div class="photo night" style="right:0;top:0;width:190px;height:218px" role="img" aria-label="Night photograph of a bridge with light trails"></div>
  <span class="tag"></span>
</section>

<!-- 10 creative brand marks -->
<section class="slide">
  <p class="hd">Creative</p>
  <div class="row" style="margin-top:10px;justify-content:space-between">
    <svg width="40" height="26"><rect width="40" height="26" rx="3" fill="var(--ink)"/></svg>
    <svg width="26" height="26"><circle cx="13" cy="13" r="13" fill="var(--ink)"/></svg>
    <svg width="40" height="26"><rect width="40" height="26" fill="none" stroke="var(--ink)" stroke-width="2"/></svg>
    <svg width="26" height="26"><circle cx="13" cy="13" r="12" fill="none" stroke="var(--ink)" stroke-width="2"/></svg>
    <svg width="40" height="26"><rect width="40" height="26" fill="var(--grey)"/></svg>
  </div>
  <div style="background:var(--ink);color:#fff;text-align:center;margin:12px 0;padding:7px" class="lbl">Flint Yard Brand</div>
  <div class="row" style="justify-content:space-between">
    <svg width="26" height="26"><circle cx="13" cy="13" r="13" fill="var(--grey)"/></svg>
    <svg width="40" height="26"><rect width="40" height="26" fill="var(--ink)"/></svg>
    <svg width="26" height="26"><circle cx="13" cy="13" r="12" fill="none" stroke="var(--ink)" stroke-width="2"/></svg>
    <svg width="40" height="26"><rect width="40" height="26" rx="3" fill="none" stroke="var(--ink)" stroke-width="2"/></svg>
    <svg width="26" height="26"><circle cx="13" cy="13" r="13" fill="var(--ink)"/></svg>
  </div>
  <span class="tag"></span>
</section>

<!-- 11 text area beige -->
<section class="slide" style="background:var(--stone)">
  <p class="hd">Text area</p>
  <div class="photo" style="left:20px;top:48px;width:120px;height:130px" role="img" aria-label="Grey workspace photograph"></div>
  <div class="abs" style="left:156px;top:52px;width:210px">
    <p class="lbl">Your subtitle here</p>
    <p class="p" style="color:#444;margin-top:4px">Short supporting copy for this point and a second short line to fill the space nicely</p>
    <p class="p" style="color:#444;margin-top:6px">Short supporting copy for this point and another line</p>
  </div>
  <span class="tag"></span>
</section>

<!-- 12 vision mission -->
<section class="slide" style="padding:0">
  <div class="photo night" style="left:0;top:0;width:388px;height:70px" role="img" aria-label="Dark city photograph banner"></div>
  <p class="hd abs" style="left:20px;top:26px;color:#fff">Our vision &amp; mission</p>
  <div class="abs" style="left:20px;top:86px;width:340px">
    <div class="item"><span class="dot"></span><div><p class="lbl">Vision</p><p class="p">Short supporting copy for this point</p></div></div>
    <div class="item"><span class="dot"></span><div><p class="lbl">Mission</p><p class="p">Short supporting copy for this point</p></div></div>
    <div class="item"><span class="dot"></span><div><p class="lbl">Values</p><p class="p">Short supporting copy for this point</p></div></div>
  </div>
  <span class="tag"></span>
</section>

<!-- 13 text area framed -->
<section class="slide" style="box-shadow:inset 0 0 0 6px var(--mist)">
  <p class="hd" style="margin-top:8px">Text area</p>
  <div class="row" style="margin-top:14px">
    <p class="p col">Short supporting copy for this point and a second line that keeps the column balanced</p>
    <p class="p col">Short supporting copy for this point and a second line that keeps the column balanced</p>
  </div>
  <div class="abs" style="right:24px;top:22px"><span class="logo">FLINT YARD</span></div>
  <span class="tag"></span>
</section>

<!-- 14 logo on frame -->
<section class="slide" style="background:var(--mist);display:flex;align-items:center;justify-content:center">
  <span class="logo" style="font-size:18px;padding:16px 22px">FLINT YARD STRATEGY</span>
  <span class="tag"></span>
</section>

<!-- 15 title with images -->
<section class="slide">
  <p class="hd">Your title goes here</p>
  <div class="abs" style="left:20px;top:50px;width:110px;height:120px;background:var(--gold);padding:10px">
    <p class="lbl">Feature</p><p class="p" style="color:var(--ink)">Short supporting copy for this point</p>
  </div>
  <div class="photo" style="left:138px;top:50px;width:110px;height:56px" role="img" aria-label="City photograph"></div>
  <div class="photo" style="left:256px;top:50px;width:110px;height:56px" role="img" aria-label="Street photograph"></div>
  <div class="photo night" style="left:138px;top:114px;width:228px;height:56px" role="img" aria-label="Building photograph"></div>
  <span class="tag"></span>
</section>

<!-- 16 photo quote -->
<section class="slide dark" style="padding:0">
  <div class="photo" style="left:0;top:0;width:194px;height:218px" role="img" aria-label="Black and white photograph of a dome"></div>
  <p class="hd abs" style="left:30px;top:40px;width:150px;color:#fff;font-size:15px">Ideas that move the market forward and stay there</p>
  <p class="p abs" style="left:210px;top:60px;width:160px">Short supporting copy for this point and a short follow on line</p>
</section>

<!-- 17 two column description bars -->
<section class="slide">
  <p class="hd">Two column description</p>
  <div class="row" style="margin-top:16px">
    <div class="col">
      <div class="bar" style="background:var(--ink)">Research</div>
      <div class="bar" style="background:var(--gold)">Planning</div>
      <div class="bar" style="background:var(--ink)">Delivery</div>
      <div class="bar" style="background:var(--gold)">Review</div>
    </div>
    <div class="col"><p class="p">Short supporting copy for this point and a second line that keeps the column balanced neatly</p></div>
  </div>
  <span class="tag"></span>
</section>

<!-- 18 dark logo -->
<section class="slide dark" style="display:flex;align-items:center;justify-content:center">
  <span class="logo" style="border:1px solid #fff">FLINT YARD STRATEGY</span>
  <span class="tag"></span>
</section>

<!-- 19 two column text -->
<section class="slide">
  <p class="hd">Two column description</p>
  <div class="row" style="margin-top:14px">
    <div class="col"><p class="lbl">First point</p><p class="p">Short supporting copy for this point with more detail</p></div>
    <div class="col"><p class="lbl">Second point</p><p class="p">Short supporting copy for this point with more detail</p></div>
  </div>
  <span class="tag"></span>
</section>

<!-- 20 title with list -->
<section class="slide">
  <p class="hd">Your title goes here</p>
  <div style="margin-top:14px;width:230px">
    <div class="bar" style="background:var(--gold)">First step</div>
    <div class="bar" style="background:var(--grey)">Second step</div>
    <div class="bar" style="background:var(--ink)">Third step</div>
    <div class="bar" style="background:var(--gold)">Fourth step</div>
  </div>
  <span class="tag"></span>
</section>

<!-- 21 bullets with paragraph -->
<section class="slide">
  <p class="hd">Your bullets with paragraph</p>
  <div class="row" style="margin-top:14px">
    <div class="col">
      <div class="item"><span class="dot"></span><p class="p">Short supporting copy for this point</p></div>
      <div class="item"><span class="dot"></span><p class="p">Short supporting copy for this point</p></div>
    </div>
    <div class="col">
      <div class="item"><span class="dot"></span><p class="p">Short supporting copy for this point</p></div>
      <div class="item"><span class="dot"></span><p class="p">Short supporting copy for this point</p></div>
    </div>
  </div>
  <span class="tag"></span>
</section>

<!-- 22 title grey box -->
<section class="slide">
  <p class="hd">Your title goes here</p>
  <div class="row" style="margin-top:12px">
    <div class="card col" style="height:120px;background:#9a9a9a;color:#fff"><p class="lbl">Highlight</p><p class="p" style="color:#eee">Short supporting copy for this point</p></div>
    <div class="col">
      <div class="item"><span class="sq g"></span><p class="p">Short supporting copy</p></div>
      <div class="item"><span class="sq"></span><p class="p">Short supporting copy</p></div>
      <div class="item"><span class="sq g"></span><p class="p">Short supporting copy</p></div>
    </div>
  </div>
  <span class="tag"></span>
</section>

<!-- 23 texts bullets -->
<section class="slide">
  <p class="hd">Texts bullets here</p>
  <div class="row" style="margin-top:14px">
    <div class="col">
      <div class="item"><span class="dot" style="background:var(--ink)"></span><p class="p">Short supporting copy</p></div>
      <div class="item"><span class="dot"></span><p class="p">Short supporting copy</p></div>
      <div class="item"><span class="dot" style="background:var(--ink)"></span><p class="p">Short supporting copy</p></div>
    </div>
    <div class="col">
      <div class="item"><span class="dot"></span><p class="p">Short supporting copy</p></div>
      <div class="item"><span class="dot" style="background:var(--ink)"></span><p class="p">Short supporting copy</p></div>
      <div class="item"><span class="dot"></span><p class="p">Short supporting copy</p></div>
    </div>
  </div>
  <span class="tag"></span>
</section>

<!-- 24 grey section -->
<section class="slide grey">
  <span class="logo" style="margin-top:46px">FLINT YARD STRATEGY</span>
  <p class="hd" style="margin-top:10px">Your title goes here</p>
  <span class="tag"></span>
</section>

<!-- 25 paragraph with other bullet -->
<section class="slide">
  <p class="hd">Paragraph with other bullet</p>
  <p class="p" style="margin-top:10px;width:300px">Short supporting copy for this point and a second line to finish the paragraph</p>
  <div class="row" style="margin-top:12px">
    <div class="card col"><span class="sq g"></span><p class="p" style="margin-top:4px">Short note</p></div>
    <div class="card col"><span class="sq"></span><p class="p" style="margin-top:4px">Short note</p></div>
    <div class="card col"><span class="sq g"></span><p class="p" style="margin-top:4px">Short note</p></div>
  </div>
  <span class="tag"></span>
</section>

<!-- 26 global reach -->
<section class="slide">
  <p class="hd">Global reach</p>
  <div class="abs" style="left:40px;top:46px;width:308px;height:140px;background:linear-gradient(180deg,#dcdcdc,#c6c6c6);border-radius:4px" role="img" aria-label="World map showing office locations"></div>
  <span class="tag"></span>
</section>

<!-- 27 chart rings -->
<section class="slide">
  <p class="hd">Your chart here</p>
  <div class="row" style="margin-top:30px;justify-content:space-around">
    <svg width="56" height="56" viewBox="0 0 36 36"><circle cx="18" cy="18" r="15.9" fill="none" stroke="var(--mist)" stroke-width="3"/><circle cx="18" cy="18" r="15.9" fill="none" stroke="var(--gold)" stroke-width="3" stroke-dasharray="70 100" transform="rotate(-90 18 18)"/><text x="18" y="21" text-anchor="middle" font-size="8" font-family="Bebas Neue">70%</text></svg>
    <svg width="56" height="56" viewBox="0 0 36 36"><circle cx="18" cy="18" r="15.9" fill="none" stroke="var(--mist)" stroke-width="3"/><circle cx="18" cy="18" r="15.9" fill="none" stroke="var(--ink)" stroke-width="3" stroke-dasharray="45 100" transform="rotate(-90 18 18)"/><text x="18" y="21" text-anchor="middle" font-size="8" font-family="Bebas Neue">45%</text></svg>
    <svg width="56" height="56" viewBox="0 0 36 36"><circle cx="18" cy="18" r="15.9" fill="none" stroke="var(--mist)" stroke-width="3"/><circle cx="18" cy="18" r="15.9" fill="none" stroke="var(--grey)" stroke-width="3" stroke-dasharray="60 100" transform="rotate(-90 18 18)"/><text x="18" y="21" text-anchor="middle" font-size="8" font-family="Bebas Neue">60%</text></svg>
    <svg width="56" height="56" viewBox="0 0 36 36"><circle cx="18" cy="18" r="15.9" fill="none" stroke="var(--mist)" stroke-width="3"/><circle cx="18" cy="18" r="15.9" fill="none" stroke="var(--gold)" stroke-width="3" stroke-dasharray="85 100" transform="rotate(-90 18 18)"/><text x="18" y="21" text-anchor="middle" font-size="8" font-family="Bebas Neue">85%</text></svg>
  </div>
  <span class="tag"></span>
</section>

<!-- 28 pie chart donut -->
<section class="slide">
  <p class="hd">Your pie chart area</p>
  <svg class="abs" style="left:40px;top:52px" width="120" height="120" viewBox="0 0 36 36">
    <circle cx="18" cy="18" r="12" fill="none" stroke="var(--ink)" stroke-width="8" stroke-dasharray="35 75.4" transform="rotate(-90 18 18)"/>
    <circle cx="18" cy="18" r="12" fill="none" stroke="var(--gold)" stroke-width="8" stroke-dasharray="0 35 22 53.4" transform="rotate(-90 18 18)"/>
    <circle cx="18" cy="18" r="12" fill="none" stroke="var(--grey)" stroke-width="8" stroke-dasharray="0 57 18.4 35" transform="rotate(-90 18 18)"/>
  </svg>
  <div class="abs" style="left:200px;top:60px;width:170px">
    <div class="item"><span class="sq"></span><p class="p">Short supporting copy</p></div>
    <div class="item"><span class="sq g"></span><p class="p">Short supporting copy</p></div>
    <div class="item"><span class="sq" style="background:var(--grey)"></span><p class="p">Short supporting copy</p></div>
  </div>
  <span class="tag"></span>
</section>

<!-- 29 pie percent -->
<section class="slide">
  <p class="hd">Your pie chart area</p>
  <svg class="abs" style="left:30px;top:60px" width="150" height="110" viewBox="0 0 150 110">
    <ellipse cx="75" cy="62" rx="70" ry="40" fill="#a87f24"/>
    <ellipse cx="75" cy="52" rx="70" ry="40" fill="var(--gold)"/>
    <path d="M75 52 L75 12 A70 40 0 0 1 140 66 Z" fill="var(--ink)"/>
  </svg>
  <div class="abs" style="left:210px;top:66px;width:160px">
    <p class="hd lg">35%</p><p class="p">Short supporting copy for this point</p>
    <p class="hd lg" style="color:var(--gold);margin-top:6px">65%</p><p class="p">Short supporting copy for this point</p>
  </div>
  <span class="tag"></span>
</section>

<!-- 30 line chart -->
<section class="slide">
  <p class="hd">This is line chart slide</p>
  <svg class="abs" style="left:100px;top:46px" width="270" height="140" viewBox="0 0 270 140">
    <g stroke="var(--mist)" stroke-width="1"><line x1="0" y1="20" x2="270" y2="20"/><line x1="0" y1="60" x2="270" y2="60"/><line x1="0" y1="100" x2="270" y2="100"/><line x1="0" y1="139" x2="270" y2="139"/></g>
    <polyline points="0,110 70,40 140,90 210,30 270,60" fill="none" stroke="var(--ink)" stroke-width="3"/>
    <polyline points="0,80 70,100 140,50 210,70 270,20" fill="none" stroke="var(--gold)" stroke-width="3"/>
  </svg>
  <p class="p abs" style="left:20px;top:60px;width:70px">Short supporting copy for this chart</p>
  <span class="tag"></span>
</section>

<!-- 31 table -->
<section class="slide">
  <p class="hd">Your table area</p>
  <table style="margin-top:10px">
    <tr><th>Item</th><th>Q1</th><th>Q2</th><th>Q3</th><th>Q4</th></tr>
    <tr><td>Reach</td><td>20</td><td>34</td><td>41</td><td>52</td></tr>
    <tr><td>Leads</td><td>12</td><td>18</td><td>26</td><td>31</td></tr>
    <tr><td>Trials</td><td>8</td><td>11</td><td>15</td><td>22</td></tr>
    <tr><td>Deals</td><td>3</td><td>5</td><td>7</td><td>9</td></tr>
    <tr><td>Renewals</td><td>2</td><td>4</td><td>5</td><td>6</td></tr>
    <tr><td>Total</td><td>45</td><td>72</td><td>94</td><td>120</td></tr>
  </table>
  <span class="tag"></span>
</section>

<!-- 32 monthly subscription -->
<section class="slide">
  <p class="hd" style="text-align:center">Monthly subscription</p>
  <div class="row" style="margin-top:10px;padding:0 24px">
    <div class="col" style="background:var(--ink);color:#fff;height:140px;padding:10px;text-align:center"><p class="lbl">Basic</p><p class="hd lg">$19</p><p class="p">Short plan note</p></div>
    <div class="col" style="background:var(--gold);height:150px;margin-top:-5px;padding:10px;text-align:center"><p class="lbl">Standard</p><p class="hd lg">$49</p><p class="p" style="color:var(--ink)">Short plan note</p></div>
    <div class="col" style="background:var(--ink);color:#fff;height:140px;padding:10px;text-align:center"><p class="lbl">Premium</p><p class="hd lg">$99</p><p class="p">Short plan note</p></div>
  </div>
  <span class="tag"></span>
</section>

<!-- 33 title with monitor -->
<section class="slide">
  <p class="hd abs" style="left:20px;top:60px;width:110px">Timeline title goes here</p>
  <p class="p abs" style="left:20px;top:100px;width:110px">Short supporting copy for this point</p>
  <div class="abs" style="left:160px;top:36px;width:206px;height:126px;background:var(--ink);padding:6px">
    <div style="width:100%;height:100%;background:linear-gradient(160deg,#cfcfcf,#6f6f6f)" role="img" aria-label="Video still shown on a desktop screen"></div>
  </div>
  <div class="abs" style="left:246px;top:162px;width:34px;height:16px;background:#bdbdbd"></div>
  <span class="tag"></span>
</section>

<!-- 34 four column -->
<section class="slide">
  <p class="hd">Four column area</p>
  <div class="row" style="margin-top:12px;gap:6px">
    <div class="col" style="background:var(--gold);height:110px;padding:8px"><p class="lbl">One</p><p class="p" style="color:var(--ink)">Short supporting copy</p></div>
    <div class="col" style="background:var(--char);height:110px;padding:8px;color:#fff"><p class="lbl">Two</p><p class="p" style="color:#ccc">Short supporting copy</p></div>
    <div class="col" style="background:var(--grey);height:110px;padding:8px;color:#fff"><p class="lbl">Three</p><p class="p" style="color:#eee">Short supporting copy</p></div>
    <div class="col" style="background:var(--gold);height:110px;padding:8px"><p class="lbl">Four</p><p class="p" style="color:var(--ink)">Short supporting copy</p></div>
  </div>
  <span class="tag"></span>
</section>

<!-- 35 four column images -->
<section class="slide">
  <p class="hd">Four column area</p>
  <div class="row" style="margin-top:12px;gap:6px">
    <div class="col"><div style="height:60px;background:var(--gold)"></div><p class="lbl" style="margin-top:5px">One</p><p class="p">Short copy</p></div>
    <div class="col"><div style="height:60px;background:linear-gradient(160deg,#d0d0d0,#777)" role="img" aria-label="Team photograph"></div><p class="lbl" style="margin-top:5px">Two</p><p class="p">Short copy</p></div>
    <div class="col"><div style="height:60px;background:var(--gold)"></div><p class="lbl" style="margin-top:5px">Three</p><p class="p">Short copy</p></div>
    <div class="col"><div style="height:60px;background:linear-gradient(160deg,#d0d0d0,#777)" role="img" aria-label="Studio photograph"></div><p class="lbl" style="margin-top:5px">Four</p><p class="p">Short copy</p></div>
  </div>
  <span class="tag"></span>
</section>

<!-- 36 work flow -->
<section class="slide">
  <p class="hd">Work flow area</p>
  <svg class="abs" style="left:20px;top:60px" width="348" height="100" viewBox="0 0 348 100">
    <path d="M10 70 A38 38 0 0 1 86 70" fill="none" stroke="var(--gold)" stroke-width="12"/>
    <path d="M96 30 A38 38 0 0 0 172 30" fill="none" stroke="var(--ink)" stroke-width="12"/>
    <path d="M182 70 A38 38 0 0 1 258 70" fill="none" stroke="var(--gold)" stroke-width="12"/>
    <path d="M268 30 A38 38 0 0 0 344 30" fill="none" stroke="var(--grey)" stroke-width="12"/>
    <circle cx="48" cy="74" r="9" fill="var(--ink)"/><circle cx="134" cy="26" r="9" fill="var(--gold)"/><circle cx="220" cy="74" r="9" fill="var(--ink)"/><circle cx="306" cy="26" r="9" fill="var(--gold)"/>
  </svg>
  <span class="tag"></span>
</section>

<!-- 37 bullets chart -->
<section class="slide">
  <p class="hd">Bullets chart area</p>
  <div class="abs" style="left:20px;top:48px;width:190px">
    <div class="item"><span class="sq"></span><p class="p">Short supporting copy</p></div>
    <div class="item"><span class="sq"></span><p class="p">Short supporting copy</p></div>
    <div class="item"><span class="sq g"></span><p class="p">Short supporting copy</p></div>
    <div class="item"><span class="sq"></span><p class="p">Short supporting copy</p></div>
  </div>
  <svg class="abs" style="left:240px;top:56px" width="110" height="110" viewBox="0 0 36 36">
    <circle cx="18" cy="18" r="14" fill="none" stroke="var(--mist)" stroke-width="6"/>
    <circle cx="18" cy="18" r="14" fill="none" stroke="var(--gold)" stroke-width="6" stroke-dasharray="66 88" transform="rotate(-90 18 18)"/>
    <text x="18" y="21" text-anchor="middle" font-size="8" font-family="Bebas Neue">75%</text>
  </svg>
  <span class="tag"></span>
</section>

<!-- 38 our team -->
<section class="slide">
  <p class="hd" style="font-size:22px">Our team</p>
  <div class="row" style="margin-top:10px;gap:8px">
    <div class="col"><div style="height:90px;background:linear-gradient(180deg,#c8c8c8,#8a8a8a)" role="img" aria-label="Team member portrait"></div><p class="lbl" style="margin-top:4px">Sam Reed</p><p class="p">Director</p></div>
    <div class="col"><div style="height:90px;background:linear-gradient(180deg,#c8c8c8,#8a8a8a)" role="img" aria-label="Team member portrait"></div><p class="lbl" style="margin-top:4px">Ana Cole</p><p class="p">Strategist</p></div>
    <div class="col"><div style="height:90px;background:linear-gradient(180deg,#c8c8c8,#8a8a8a)" role="img" aria-label="Team member portrait"></div><p class="lbl" style="margin-top:4px">Tom Hale</p><p class="p">Designer</p></div>
    <div class="col"><div style="height:90px;background:linear-gradient(180deg,#c8c8c8,#8a8a8a)" role="img" aria-label="Team member portrait"></div><p class="lbl" style="margin-top:4px">Lia Moss</p><p class="p">Analyst</p></div>
  </div>
  <span class="tag"></span>
</section>

<!-- 39 thank you -->
<section class="slide dark" style="display:flex;flex-direction:column;align-items:center;justify-content:center">
  <span class="logo" style="border:1px solid #fff">FLINT YARD STRATEGY</span>
  <p class="hd" style="margin-top:10px;font-size:13px">Thank you</p>
</section>

</main>
</body>
</html>
```